Business Card Design

Needing a business card design similar to the business card that is attached.

Industry/Entity Type

Business

Contact Information for Business Card

Design similar to the b-cards that is attached.

```html
<!DOCTYPE html>
<html lang="en">
<head>
<meta charset="utf-8">
<title>Business Card</title>
<link rel="stylesheet" href="https://fonts.googleapis.com/css2?family=Cutive+Mono&display=swap">
<style>
  :root {
    --card-gold: #a88a2c;
    --card-gold-light: #b39731;
    --card-gold-deep: #9a7d24;
    --band-dark: rgba(120, 92, 20, 0.22);
    --band-light: rgba(205, 176, 80, 0.16);
    --ink-brown: #2e1608;
    --ornament-brown: rgba(84, 42, 18, 0.42);
    --ornament-brown-strong: rgba(84, 42, 18, 0.62);
    --ornament-edge: rgba(84, 42, 18, 0.18);
  }
  html, body {
    margin: 0;
    padding: 0;
    width: 1200px;
    height: 702px;
    overflow: hidden;
    background: #ffffff;
  }
  .business-card {
    position: relative;
    width: 1200px;
    height: 702px;
    overflow: hidden;
    background:
      repeating-linear-gradient(180deg,
        transparent 0px, transparent 14px,
        var(--band-dark) 14px, var(--band-dark) 18px,
        transparent 18px, transparent 26px,
        var(--band-light) 26px, var(--band-light) 30px,
        transparent 30px, transparent 36px),
      linear-gradient(180deg, var(--card-gold-light) 0%, var(--card-gold) 50%, var(--card-gold-deep) 100%);
    font-family: "Cutive Mono", "Courier New", monospace;
    color: var(--ink-brown);
  }
  .ornament {
    position: absolute;
    box-sizing: border-box;
    border: 1px solid var(--ornament-edge);
  }
  .ornament--butterflies-left {
    left: 6px; top: 14px; width: 176px; height: 128px;
    border-radius: 46% 54% 50% 50% / 50% 50% 50% 50%;
    background: linear-gradient(135deg, var(--ornament-brown-strong) 0%, var(--ornament-brown) 100%);
  }
  .ornament--swirl-top-right {
    left: 882px; top: 18px; width: 318px; height: 290px;
    border-radius: 100% 0 0 100% / 60% 0 0 100%;
    background: linear-gradient(225deg, var(--ornament-brown) 0%, rgba(84, 42, 18, 0.22) 100%);
  }
  .ornament--flourish-center {
    left: 240px; top: 250px; width: 693px; height: 122px;
    border-radius: 50%;
    background: linear-gradient(90deg, var(--ornament-brown) 0%, var(--ornament-brown-strong) 50%, var(--ornament-brown) 100%);
  }
  .ornament--vine-left {
    left: 0; top: 350px; width: 178px; height: 352px;
    border-left: none;
    border-radius: 0 60% 40% 0 / 0 50% 50% 0;
    background: linear-gradient(180deg, rgba(84, 42, 18, 0.28) 0%, var(--ornament-brown) 100%);
  }
  .ornament--flowers-bottom-right {
    left: 742px; top: 356px; width: 458px; height: 346px;
    border-right: none; border-bottom: none;
    border-radius: 100% 0 0 0 / 100% 0 0 0;
    background: linear-gradient(315deg, rgba(70, 34, 14, 0.78) 0%, var(--ornament-brown-strong) 55%, var(--ornament-brown) 100%);
  }
  .heading-line {
    position: absolute;
    margin: 0;
    font-weight: 400;
    line-height: 1;
    white-space: nowrap;
    -webkit-text-stroke: 1px var(--ink-brown);
  }
  .heading-line--trim {
    right: 370px;
    top: 64px;
    font-size: 80px;
    letter-spacing: -2px;
  }
  .heading-line--safe-margin {
    left: 321px;
    top: 165px;
    font-size: 78px;
  }
  .contact-list {
    position: absolute;
    left: 144px;
    top: 438px;
    margin: 0;
    padding: 0;
    list-style: none;
    font-size: 27px;
    line-height: 44px;
    -webkit-text-stroke: 0.6px var(--ink-brown);
  }
</style>
</head>
<body>
  <main class="business-card">
    <div class="ornament ornament--butterflies-left" role="img" aria-label="Two brown butterfly silhouettes"></div>
    <div class="ornament ornament--swirl-top-right" role="img" aria-label="Brown swirling vine with small butterflies"></div>
    <div class="ornament ornament--flourish-center" role="img" aria-label="Symmetrical brown scroll flourish divider"></div>
    <div class="ornament ornament--vine-left" role="img" aria-label="Brown curling vine ornament"></div>
    <div class="ornament ornament--flowers-bottom-right" role="img" aria-label="Cluster of stylised brown retro flowers and circles"></div>

    <h1 class="heading-line heading-line--trim">TRIM</h1>
    <h2 class="heading-line heading-line--safe-margin">SAFE MARGIN</h2>

    <ul class="contact-list">
      <li class="contact-list__item">Tel:+*** ******</li>
      <li class="contact-list__item">Website: ******@***.com</li>
      <li class="contact-list__item">Office address: ***** *** ***** *</li>
    </ul>
  </main>
</body>
</html>
```